Trainingsplaner 2014_KV

We would like to design a planer for our actual workshops. The planer should be for the whole of 2014 - please have a look at the enclosed file (Training Agenda) where you can find more details.
You'll also find our actual KVR_Booklet_P1 (Trainingsprogram) to give you the idea about the style we are using. As well as R4 Seminarkalender (as an idea) and an excel file (Trainingagenda_2014) with the actual dates of the workshops. Please also note that when you have a workshop or an event taking more than one day, that you visualize it over two or more days in one mention.
The planer size should be A3 cross and we would need print files.
The matter is very urgent! for any other question please don't hesitate to contact me, with my best regards
Wilma
Target Market(s)
Hairdressers of any age, very visual driven people
Industry/Entity Type
Training
Requirements
Must have
- The planer has to be A3 cross, months (vertical) and days (horizontal) have a look at the samples.

```html
<!DOCTYPE html>
<html lang="de">
<head>
<meta charset="utf-8">
<title>Trainingsplaner 2014 – Kara Velde</title>
<link href="https://fonts.googleapis.com/css2?family=Source+Sans+3:wght@400;600;700&display=swap" rel="stylesheet">
<style>
:root{
  --ink-dark:#2a2a2a;
  --white:#ffffff;
  --accent-red:#e8433f;
  --band-red:#e9473f;
  --event-blue:#3f8fd2;
  --event-gold:#f7c418;
  --cell-weekday:rgba(160,160,160,.78);
  --cell-weekend:rgba(236,236,236,.92);
  --cell-blank:rgba(72,72,72,.95);
  --grid-line:rgba(255,255,255,.45);
  --text-dark:#333333;
}
*{box-sizing:border-box;margin:0;padding:0}
html,body{width:1200px;height:848px;overflow:hidden}
body{font-family:"Source Sans 3",sans-serif;background:var(--ink-dark)}
.planner{position:relative;width:1200px;height:848px;overflow:hidden}
.backdrop{position:absolute;inset:0;
  background:
    radial-gradient(ellipse 520px 460px at 1080px 220px,rgba(235,235,235,.85),rgba(235,235,235,0) 70%),
    linear-gradient(90deg,#2a2a2a 0%,#3a3a3a 30%,#8a8a8a 62%,#c8c8c8 85%,#9a9a9a 100%);}
.title{position:absolute;left:36px;top:22px;color:var(--white);font-weight:700;font-size:50px;letter-spacing:-.3px;line-height:1}
.intro{position:absolute;left:50px;top:88px;color:var(--white);font-size:15px;line-height:18.5px;font-weight:400}
.brand{position:absolute;left:884px;top:48px;width:276px;height:73px;background:var(--white);
  display:flex;align-items:center;justify-content:center;gap:8px}
.brand-mark{width:14px;height:14px;background:var(--text-dark)}
.brand-name{font-weight:600;font-size:22px;color:var(--text-dark);letter-spacing:1px}
.day-numbers{position:absolute;left:108px;top:162px;width:1058px;display:grid;grid-template-columns:repeat(31,1fr);gap:0 1px}
.day-numbers span{text-align:center;color:var(--accent-red);font-size:13px}
.months{position:absolute;left:0;top:190px;width:98px;height:628px;display:grid;grid-template-rows:repeat(12,1fr)}
.months span{color:var(--accent-red);font-size:14px;text-align:right;align-self:center}
.calendar{position:absolute;left:108px;top:190px;width:1058px;height:628px;display:grid;
  grid-template-columns:repeat(31,1fr);grid-template-rows:repeat(12,1fr);gap:1px;background:var(--grid-line);border:1px solid #111}
.day{background:var(--cell-weekday);display:flex;flex-direction:column;align-items:center;padding:2px 1px;min-width:0;overflow:hidden}
.day b{align-self:flex-start;font-weight:400;font-size:9px;color:var(--text-dark);padding-left:3px}
.day span{font-size:5.2px;line-height:1.15;text-align:center;color:var(--text-dark);margin-top:12px;word-break:break-word}
.day span.low{margin-top:auto;margin-bottom:1px}
.end{background:var(--cell-weekend)}
.light{background:var(--cell-weekend)}
.blank{background:var(--cell-blank)}
.blue{background:var(--event-blue)}
.blue b,.blue span{color:var(--white)}
.gold{background:var(--event-gold)}
.hol b{color:var(--accent-red)}
.bands{position:absolute;left:109px;top:191px;width:1056px;height:626px;display:grid;
  grid-template-columns:repeat(31,1fr);grid-template-rows:repeat(12,1fr);gap:1px;pointer-events:none}
.band{background:var(--band-red);color:var(--white);font-size:5.4px;line-height:1.1;text-align:center;
  align-self:start;margin-top:24px;padding:1px 2px;min-height:9px;display:flex;align-items:center;justify-content:center}
.band.tall{min-height:13px}
</style>
</head>
<body>
<div class="planner">
  <div class="backdrop" role="img" aria-label="Black-and-white photograph of a model with long flowing hair on the right side"></div>

  <h1 class="title">Trainingsplaner 2014</h1>
  <p class="intro">Wir freuen uns über Ihre Anmeldung auf www.karavelde.ch<br>Oder 044 555 71 20.<br>Footnote: Änderungen vorbehalten.</p>

  <div class="brand"><i class="brand-mark"></i><span class="brand-name">KARA VELDE</span></div>

  <div class="day-numbers">
    <span>01.</span><span>02.</span><span>03.</span><span>04.</span><span>05.</span><span>06.</span><span>07.</span><span>08.</span><span>09.</span><span>10.</span><span>11.</span><span>12.</span><span>13.</span><span>14.</span><span>15.</span><span>16.</span><span>17.</span><span>18.</span><span>19.</span><span>20.</span><span>21.</span><span>22.</span><span>23.</span><span>24.</span><span>25.</span><span>26.</span><span>27.</span><span>28.</span><span>29.</span><span>30.</span><span>31.</span>
  </div>

  <div class="months">
    <span>Januar</span><span>Februar</span><span>März</span><span>April</span><span>Mai</span><span>Juni</span><span>Juli</span><span>August</span><span>September</span><span>Oktober</span><span>November</span><span>Dezember</span>
  </div>

  <div class="calendar">
    <!-- Januar -->
    <div class="day hol"><b>Mi</b></div><div class="day"><b>Do</b></div><div class="day"><b>Fr</b></div><div class="day end"><b>Sa</b></div><div class="day end"><b>So</b></div><div class="day"><b>Mo</b></div><div class="day"><b>Di</b></div><div class="day"><b>Mi</b></div><div class="day"><b>Do</b></div><div class="day"><b>Fr</b></div><div class="day end"><b>Sa</b></div><div class="day end"><b>So</b></div><div class="day"><b>Mo</b></div><div class="day"><b>Di</b></div><div class="day"><b>Mi</b></div><div class="day"><b>Do</b></div><div class="day"><b>Fr</b></div><div class="day end"><b>Sa</b></div><div class="day end"><b>So</b></div><div class="day gold"><b>Mo</b><span>Principles of Coloring</span></div><div class="day"><b>Di</b></div><div class="day"><b>Mi</b></div><div class="day"><b>Do</b></div><div class="day"><b>Fr</b></div><div class="day end"><b>Sa</b></div><div class="day end"><b>So</b></div><div class="day"><b>Mo</b></div><div class="day"><b>Di</b></div><div class="day"><b>Mi</b></div><div class="day"><b>Do</b></div><div class="day"><b>Fr</b></div>
    <!-- Februar -->
    <div class="day end"><b>Sa</b></div><div class="day end"><b>So</b></div><div class="day blue"><b>Mo</b><span>Collection Cut &amp; Color Spring 2014</span></div><div class="day"><b>Di</b></div><div class="day"><b>Mi</b></div><div class="day"><b>Do</b></div><div class="day"><b>Fr</b></div><div class="day end"><b>Sa</b></div><div class="day blue"><b>So</b><span>Gesichtlesen mit Marco Lenti</span></div><div class="day blue"><b>Mo</b><span>Principles of Texture</span></div><div class="day"><b>Di</b></div><div class="day"><b>Mi</b></div><div class="day"><b>Do</b></div><div class="day"><b>Fr</b></div><div class="day end"><b>Sa</b></div><div class="day end"><b>So</b></div><div class="day blue"><b>Mo</b><span>Principles of Coloring</span></div><div class="day"><b>Di</b></div><div class="day"><b>Mi</b></div><div class="day"><b>Do</b></div><div class="day"><b>Fr</b></div><div class="day end"><b>Sa</b></div><div class="day blue"><b>So</b><span>hdx Professional Stylist</span></div><div class="day gold"><b>Mo</b><span>hdx Professional Stylist</span></div><div class="day"><b>Di</b></div><div class="day"><b>Mi</b></div><div class="day"><b>Do</b></div><div class="day"><b>Fr</b></div><div class="day blank"></div><div class="day blank"></div><div class="day blank"></div>
    <!-- März -->
    <div class="day end"><b>Sa</b></div><div class="day end"><b>So</b></div><div class="day gold"><b>Mo</b><span>Principles of Coloring</span></div><div class="day"><b>Di</b></div><div class="day"><b>Mi</b></div><div class="day"><b>Do</b></div><div class="day"><b>Fr</b></div><div class="day end"><b>Sa</b></div><div class="day gold"><b>So</b></div><div class="day gold"><b>Mo</b></div><div class="day"><b>Di</b></div><div class="day"><b>Mi</b></div><div class="day"><b>Do</b></div><div class="day"><b>Fr</b></div><div class="day end"><b>Sa</b></div><div class="day end"><b>So</b></div><div class="day gold"><b>Mo</b><span>Principles of Haircutting</span></div><div class="day"><b>Di</b></div><div class="day"><b>Mi</b></div><div class="day"><b>Do</b></div><div class="day"><b>Fr</b></div><div class="day gold"><b>Sa</b></div><div class="day gold"><b>So</b></div><div class="day gold"><b>Mo</b><span>hdx Professional Stylist</span></div><div class="day"><b>Di</b></div><div class="day"><b>Mi</b></div><div class="day"><b>Do</b></div><div class="day"><b>Fr</b></div><div class="day end"><b>Sa</b></div><div class="day end"><b>So</b></div><div class="day light"><b>Mo</b><span>Style Notes</span></div>
    <!-- April -->
    <div class="day"><b>Di</b></div><div class="day"><b>Mi</b></div><div class="day"><b>Do</b></div><div class="day blue"><b>Fr</b></div><div class="day blue"><b>Sa</b></div><div class="day blue"><b>So</b></div><div class="day blue"><b>Mo</b><span class="low">Principles of Coloring</span></div><div class="day"><b>Di</b></div><div class="day"><b>Mi</b></div><div class="day"><b>Do</b></div><div class="day"><b>Fr</b></div><div class="day end"><b>Sa</b></div><div class="day end"><b>So</b></div><div class="day blue"><b>Mo</b><span>Ready for Short Hair</span></div><div class="day"><b>Di</b></div><div class="day"><b>Mi</b></div><div class="day"><b>Do</b></div><div class="day hol"><b>Fr</b></div><div class="day end"><b>Sa</b></div><div class="day end hol"><b>So</b></div><div class="day hol"><b>Mo</b></div><div class="day"><b>Di</b></div><div class="day"><b>Mi</b></div><div class="day"><b>Do</b></div><div class="day"><b>Fr</b></div><div class="day end"><b>Sa</b></div><div class="day end"><b>So</b></div><div class="day"><b>Mo</b></div><div class="day"><b>Di</b></div><div class="day"><b>Mi</b></div><div class="day blank"></div>
    <!-- Mai -->
    <div class="day hol"><b>Do</b></div><div class="day"><b>Fr</b></div><div class="day end"><b>Sa</b></div><div class="day end"><b>So</b></div><div class="day gold"><b>Mo</b><span>Principles of Coloring</span></div><div class="day"><b>Di</b></div><div class="day"><b>Mi</b></div><div class="day"><b>Do</b></div><div class="day"><b>Fr</b></div><div class="day end"><b>Sa</b></div><div class="day end"><b>So</b></div><div class="day gold"><b>Mo</b><span>Ready for Curls</span></div><div class="day"><b>Di</b></div><div class="day"><b>Mi</b></div><div class="day"><b>Do</b></div><div class="day"><b>Fr</b></div><div class="day end"><b>Sa</b></div><div class="day end"><b>So</b></div><div class="day gold"><b>Mo</b><span>Principles of Texture</span></div><div class="day"><b>Di</b></div><div class="day"><b>Mi</b></div><div class="day"><b>Do</b></div><div class="day"><b>Fr</b></div><div class="day end"><b>Sa</b></div><div class="day end"><b>So</b></div><div class="day gold"><b>Mo</b><span>Insight 16</span></div><div class="day"><b>Di</b></div><div class="day"><b>Mi</b></div><div class="day hol"><b>Do</b></div><div class="day"><b>Fr</b></div><div class="day end"><b>Sa</b></div>
    <!-- Juni -->
    <div class="day end"><b>So</b></div><div class="day blue"><b>Mo</b><span>hdx Collection - Gala Night</span></div><div class="day"><b>Di</b></div><div class="day"><b>Mi</b></div><div class="day"><b>Do</b></div><div class="day"><b>Fr</b></div><div class="day end"><b>Sa</b></div><div class="day end hol"><b>So</b></div><div class="day hol"><b>Mo</b></div><div class="day"><b>Di</b></div><div class="day"><b>Mi</b></div><div class="day"><b>Do</b></div><div class="day"><b>Fr</b></div><div class="day end"><b>Sa</b></div><div class="day end"><b>So</b></div><div class="day blue"><b>Mo</b><span>Principles of Coloring</span></div><div class="day"><b>Di</b></div><div class="day"><b>Mi</b></div><div class="day"><b>Do</b></div><div class="day"><b>Fr</b></div><div class="day end"><b>Sa</b></div><div class="day end"><b>So</b></div><div class="day blue"><b>Mo</b><span>Principles of Styling</span></div><div class="day"><b>Di</b></div><div class="day"><b>Mi</b></div><div class="day"><b>Do</b></div><div class="day"><b>Fr</b></div><div class="day end"><b>Sa</b></div><div class="day end"><b>So</b></div><div class="day"><b>Mo</b></div><div class="day blank"></div>
    <!-- Juli -->
    <div class="day"><b>Di</b></div><div class="day"><b>Mi</b></div><div class="day"><b>Do</b></div><div class="day"><b>Fr</b></div><div class="day end"><b>Sa</b></div><div class="day end"><b>So</b></div><div class="day gold"><b>Mo</b><span>Principles of Coloring</span></div><div class="day"><b>Di</b></div><div class="day"><b>Mi</b></div><div class="day"><b>Do</b></div><div class="day"><b>Fr</b></div><div class="day end"><b>Sa</b></div><div class="day end"><b>So</b></div><div class="day gold"><b>Mo</b><span>Ready for Curls</span></div><div class="day"><b>Di</b></div><div class="day"><b>Mi</b></div><div class="day"><b>Do</b></div><div class="day"><b>Fr</b></div><div class="day end"><b>Sa</b></div><div class="day end"><b>So</b></div><div class="day gold"><b>Mo</b><span>hdx Professional Stylist</span></div><div class="day"><b>Di</b></div><div class="day"><b>Mi</b></div><div class="day"><b>Do</b></div><div class="day"><b>Fr</b></div><div class="day end"><b>Sa</b></div><div class="day end"><b>So</b></div><div class="day"><b>Mo</b></div><div class="day"><b>Di</b></div><div class="day"><b>Mi</b></div><div class="day"><b>Do</b></div>
    <!-- August -->
    <div class="day"><b>Fr</b></div><div class="day end"><b>Sa</b></div><div class="day end"><b>So</b></div><div class="day blue"><b>Mo</b><span class="low">Principles of Coloring</span></div><div class="day blue"><b>Di</b></div><div class="day"><b>Mi</b></div><div class="day"><b>Do</b></div><div class="day"><b>Fr</b></div><div class="day end"><b>Sa</b></div><div class="day end"><b>So</b></div><div class="day blue"><b>Mo</b><span>Principles of Styling</span></div><div class="day"><b>Di</b></div><div class="day"><b>Mi</b></div><div class="day"><b>Do</b></div><div class="day"><b>Fr</b></div><div class="day end"><b>Sa</b></div><div class="day end"><b>So</b></div><div class="day blue"><b>Mo</b><span>Principles of Texture</span></div><div class="day"><b>Di</b></div><div class="day"><b>Mi</b></div><div class="day"><b>Do</b></div><div class="day"><b>Fr</b></div><div class="day end"><b>Sa</b></div><div class="day blue"><b>So</b><span>hdx Collection</span></div><div class="day"><b>Mo</b></div><div class="day"><b>Di</b></div><div class="day"><b>Mi</b></div><div class="day"><b>Do</b></div><div class="day"><b>Fr</b></div><div class="day end"><b>Sa</b></div><div class="day end"><b>So</b></div>
    <!-- September -->
    <div class="day gold"><b>Mo</b><span>Collection Cut &amp; Color Fall 2014 Share Color - not Trends</span></div><div class="day"><b>Di</b></div><div class="day"><b>Mi</b></div><div class="day"><b>Do</b></div><div class="day"><b>Fr</b></div><div class="day end"><b>Sa</b></div><div class="day end"><b>So</b></div><div class="day gold"><b>Mo</b><span>Principles of Coloring</span></div><div class="day"><b>Di</b></div><div class="day"><b>Mi</b></div><div class="day"><b>Do</b></div><div class="day"><b>Fr</b></div><div class="day end"><b>Sa</b></div><div class="day end"><b>So</b></div><div class="day gold"><b>Mo</b><span>Principles of Haircutting</span></div><div class="day"><b>Di</b></div><div class="day"><b>Mi</b></div><div class="day"><b>Do</b></div><div class="day"><b>Fr</b></div><div class="day end"><b>Sa</b></div><div class="day end"><b>So</b></div><div class="day gold"><b>Mo</b><span>Principles of Styling</span></div><div class="day"><b>Di</b></div><div class="day"><b>Mi</b></div><div class="day"><b>Do</b></div><div class="day"><b>Fr</b></div><div class="day end"><b>Sa</b></div><div class="day end"><b>So</b></div><div class="day"><b>Mo</b></div><div class="day"><b>Di</b></div><div class="day blank"></div>
    <!-- Oktober -->
    <div class="day"><b>Mi</b></div><div class="day"><b>Do</b></div><div class="day hol"><b>Fr</b></div><div class="day end"><b>Sa</b></div><div class="day end"><b>So</b></div><div class="day blue"><b>Mo</b><span>Principles of Coloring</span></div><div class="day"><b>Di</b></div><div class="day"><b>Mi</b></div><div class="day"><b>Do</b></div><div class="day"><b>Fr</b></div><div class="day blue"><b>Sa</b></div><div class="day blue"><b>So</b></div><div class="day blue"><b>Mo</b><span class="low">Ready for Short Hair</span></div><div class="day"><b>Di</b></div><div class="day"><b>Mi</b></div><div class="day"><b>Do</b></div><div class="day"><b>Fr</b></div><div class="day end"><b>Sa</b></div><div class="day end"><b>So</b></div><div class="day blue"><b>Mo</b><span class="low">Salon Care</span></div><div class="day"><b>Di</b></div><div class="day"><b>Mi</b></div><div class="day"><b>Do</b></div><div class="day"><b>Fr</b></div><div class="day end"><b>Sa</b></div><div class="day blue"><b>So</b></div><div class="day blue"><b>Mo</b></div><div class="day"><b>Di</b></div><div class="day"><b>Mi</b></div><div class="day"><b>Do</b></div><div class="day"><b>Fr</b></div>
    <!-- November -->
    <div class="day end"><b>Sa</b></div><div class="day end"><b>So</b></div><div class="day gold"><b>Mo</b><span>Principles of Coloring</span></div><div class="day"><b>Di</b></div><div class="day"><b>Mi</b></div><div class="day"><b>Do</b></div><div class="day"><b>Fr</b></div><div class="day end"><b>Sa</b></div><div class="day end"><b>So</b></div><div class="day"><b>Mo</b></div><div class="day"><b>Di</b></div><div class="day"><b>Mi</b></div><div class="day"><b>Do</b></div><div class="day"><b>Fr</b></div><div class="day end"><b>Sa</b></div><div class="day end"><b>So</b></div><div class="day gold"><b>Mo</b><span>hdx Professional Stylist</span></div><div class="day"><b>Di</b></div><div class="day"><b>Mi</b></div><div class="day"><b>Do</b></div><div class="day"><b>Fr</b></div><div class="day end"><b>Sa</b></div><div class="day end"><b>So</b></div><div class="day gold"><b>Mo</b><span>Holiday Longhair Collection</span></div><div class="day"><b>Di</b></div><div class="day"><b>Mi</b></div><div class="day"><b>Do</b></div><div class="day"><b>Fr</b></div><div class="day end"><b>Sa</b></div><div class="day end"><b>So</b></div><div class="day blank"></div>
    <!-- Dezember -->
    <div class="day blue"><b>Mo</b><span>Principles of Styling</span></div><div class="day"><b>Di</b></div><div class="day"><b>Mi</b></div><div class="day"><b>Do</b></div><div class="day"><b>Fr</b></div><div class="day end"><b>Sa</b></div><div class="day end"><b>So</b></div><div class="day blue"><b>Mo</b><span>Principles of Coloring</span></div><div class="day"><b>Di</b></div><div class="day"><b>Mi</b></div><div class="day"><b>Do</b></div><div class="day"><b>Fr</b></div><div class="day end"><b>Sa</b></div><div class="day end"><b>So</b></div><div class="day"><b>Mo</b></div><div class="day"><b>Di</b></div><div class="day"><b>Mi</b></div><div class="day"><b>Do</b></div><div class="day"><b>Fr</b></div><div class="day end"><b>Sa</b></div><div class="day end"><b>So</b></div><div class="day"><b>Mo</b></div><div class="day"><b>Di</b></div><div class="day"><b>Mi</b></div><div class="day hol"><b>Do</b></div><div class="day hol"><b>Fr</b></div><div class="day end"><b>Sa</b></div><div class="day end"><b>So</b></div><div class="day"><b>Mo</b></div><div class="day"><b>Di</b></div><div class="day"><b>Mi</b></div>
  </div>

  <div class="bands">
    <div class="band tall" style="grid-row:3;grid-column:9/11">Long Hair Lover with<br>Paola Rinaldi</div>
    <div class="band" style="grid-row:3;grid-column:22/24">Hair Forum, Düsseldorf</div>
    <div class="band" style="grid-row:4;grid-column:4/8;margin-top:19px">Beauty Expo, Bologna</div>
    <div class="band tall" style="grid-row:8;grid-column:4/6;margin-top:13px">The Stylist Summit<br>Las Vegas</div>
    <div class="band" style="grid-row:10;grid-column:11/14">Salon Week, London</div>
    <div class="band tall" style="grid-row:10;grid-column:26/28">Haartage,<br>Seewald</div>
  </div>
</div>
</body>
</html>
```